South Florida Real Estate Brokerage Business

The name is DWELL VANTORO REAL ESTATE.
The company is a Real estate realty based in Miami.
Is targeted to Latin American clients.
Must express luxury, and efficiency.
Target clients for properties around 250k to a million +.
Vantoro means Royal in Latin.
Should communicate safety and knowledge of the product and transaction with a tech edge.

The web design needs to be a Social tool, with Chatterloop and other media integration of some sort. Needs to have a Show case place, a Search place (MLS listings) with maps and filters.
Needs to reflect luxury but also mixed with a social edge capable of engaging clients or transition them to communicate with the page.
Include the logo from the uploaded files, feel free to change the color or font per webdesign.
This is a Front en design, layout and graphics.
Possible future programming if approved.
I can receive Quotes for the Code part.

Target Market(s)

Spanish and English speakers living in Latin America and Canada looking for apartments and houses to buy.

Industry/Entity Type

Business

Requirements
Must have
• Search area.
Neighbourhood area.
Could be a blog or news area.
Client registration.
Social Plugin
Nice to have
• Social linking to networks.
Log in with chatterloop account.
Chatterloop Like.

```html
<!DOCTYPE html>
<html lang="en">
<head>
<meta charset="utf-8">
<title>Dwell Vantoro Real Estate</title>
<link rel="stylesheet" href="https://fonts.googleapis.com/css2?family=Cinzel:wght@400;600&family=Ubuntu:wght@300;400;500&family=Open+Sans:wght@400;600&family=PT+Serif:wght@400;700&display=swap">
<style>
:root{
  --dark:#2a2522;
  --dark-2:#3a3431;
  --gold:#c9a862;
  --gold-soft:#d8bd84;
  --orange:#d9542c;
  --ink:#333;
  --muted:#6b6b6b;
  --line:#d9d9d9;
  --white:#fff;
  --green:#4a9a16;
  --field:#e0e0e0;
}
*{box-sizing:border-box;margin:0;padding:0}
html,body{width:925px;height:1200px;overflow:hidden}
body{position:relative;background:var(--white);font-family:"Open Sans",Arial,sans-serif;color:var(--ink)}
.abs{position:absolute}

/* header */
.header-band{left:0;top:0;width:925px;height:382px;background:radial-gradient(ellipse at 50% 0,#3c3531 0,#2a2522 55%,#221e1c 100%)}
.header-fade{left:0;top:382px;width:925px;height:90px;background:linear-gradient(#cfcfcf,#f4f4f4 60%,#fff)}
.brand{left:108px;top:12px;width:164px;text-align:center}
.brand-mark{width:58px;height:58px;margin:0 auto 8px;background:var(--gold)}
.brand-name{font-family:"Cinzel",serif;font-weight:400;color:var(--gold);font-size:15px;line-height:18px;letter-spacing:.5px}

.login label{position:absolute;color:#fff;font-family:"Ubuntu",sans-serif;font-size:10px}
.login .field{position:absolute;height:20px;background:var(--field);border:1px solid #bbb}
.login .btn{position:absolute;left:773px;top:22px;width:44px;height:20px;background:#4d4744;color:#fff;font-size:11px;font-family:"Ubuntu",sans-serif;text-align:center;line-height:20px;border:1px solid #5e5854}
.login .check{position:absolute;left:461px;top:48px;width:10px;height:10px;background:#ddd}

.nav{left:295px;top:96px;display:flex;font-family:"Ubuntu",sans-serif;font-size:10.5px;color:#fff;text-transform:uppercase}
.nav span{padding:0 15px;line-height:15px;border-left:1px solid #8a8380}
.nav span:first-child{border-left:0;padding-left:9px}
.nav span:last-child{padding-right:0}

.slider{left:108px;top:128px;width:709px;height:302px;background:#a8a8a8}
.slide{left:116px;top:136px;width:694px;height:294px;background:linear-gradient(#a9b9c9 0,#b6c2cd 35%,#8c9a6b 70%,#4c7a2e 100%)}
.slider-shadow{left:118px;top:430px;width:690px;height:26px;background:radial-gradient(ellipse at 50% 0,rgba(0,0,0,.45),rgba(0,0,0,0) 70%)}
.arrow-btn{width:38px;height:38px;border-radius:50%;background:#fff;box-shadow:0 1px 4px rgba(0,0,0,.35)}
.arrow-btn svg{display:block;margin:12px auto}

/* search */
.tab{top:474px;height:28px;font-family:"PT Serif",serif;font-size:11px;line-height:28px;text-align:center;text-transform:uppercase;border:1px solid #cfcfcf;border-bottom:0}
.tab.active{background:linear-gradient(#fff,#ececec);color:#222}
.tab.dark{background:linear-gradient(#3e3835,#2a2522);color:#fff;border-color:#555}
.search-panel{left:108px;top:501px;width:710px;height:71px;border:1px solid #d3d3d3;background:linear-gradient(#fafafa,#ececec)}
.sp{position:absolute;font-size:9.5px;color:#444}
.select{position:absolute;height:14px;background:#fff;border:1px solid #aaa;font-size:8px;line-height:12px;padding-left:3px;color:#222}
.select::after{content:"▾";position:absolute;right:3px;top:0;font-size:8px}
.radio{position:absolute;width:9px;height:9px;border-radius:50%;border:1px solid #999;background:#fff}
.radio.on::after{content:"";position:absolute;left:2px;top:2px;width:3px;height:3px;border-radius:50%;background:#2a5aa8}
.search-btn{left:684px;top:516px;width:118px;height:26px;border-radius:4px;background:linear-gradient(#7cc241,#3f8a13);color:#fff;font-family:"Ubuntu",sans-serif;font-size:11.5px;line-height:26px;padding-left:6px}
.search-btn svg{position:absolute;right:7px;top:6px}

/* content */
.welcome-bar{left:108px;top:593px;width:328px;height:30px;background:linear-gradient(90deg,#caa767,#e1c793 55%,#fff)}
.welcome-bar::before{content:"";position:absolute;left:0;top:0;width:7px;height:30px;background:#333}
.welcome-bar h2{position:absolute;left:16px;top:5px;font-family:"Cinzel",serif;font-weight:400;font-size:17px;color:#2a2522;letter-spacing:.4px}
.copy{left:109px;width:350px;font-size:9.3px;line-height:13px;color:#333}
.more{font-size:8px;color:#555}
.news-title{left:485px;top:590px;font-family:"Ubuntu",sans-serif;font-weight:300;font-size:16px;color:#222;letter-spacing:-.3px}
.news-item h3{position:absolute;left:62px;top:0;font-family:"Ubuntu",sans-serif;font-weight:400;font-size:12px;color:#111;white-space:nowrap}
.news-item p{position:absolute;left:62px;top:18px;width:270px;font-size:9.3px;line-height:13px;color:#555}
.rule{left:200px;top:751px;width:525px;height:1px;background:linear-gradient(90deg,#fff,#ddd 20%,#ddd 80%,#fff)}
.gallery-title{left:0;top:768px;width:925px;text-align:center;font-family:"Ubuntu",sans-serif;font-size:19px;color:#333;letter-spacing:.5px}
.thumb{top:803px;width:132px;height:130px;background:#e4e4e4;border:1px solid #d2d2d2;box-shadow:0 2px 4px rgba(0,0,0,.12)}
.thumb div{position:absolute;left:8px;top:8px;width:114px;height:112px}
.gal-shadow{left:140px;top:930px;width:645px;height:26px;background:radial-gradient(ellipse at 50% 0,rgba(0,0,0,.13),rgba(0,0,0,0) 70%)}
.gal-arrow{top:846px;width:23px;height:44px;background:linear-gradient(#f2f2f2,#d8d8d8);border:1px solid #ccc}

/* footer */
.footer{left:0;top:958px;width:925px;height:242px;background:radial-gradient(ellipse at 50% 10%,#3d3633,#2a2522 60%,#221d1b)}
.f{position:absolute;font-size:8.8px;color:#c8c2bd;line-height:13px}
.f-head{position:absolute;font-size:9px;font-weight:600;color:var(--orange);text-transform:uppercase}
.newsletter{left:108px;top:978px;font-family:"Ubuntu",sans-serif;font-size:14px;color:var(--gold-soft)}
.nl-field{left:276px;top:978px;width:125px;height:20px;background:#fff;font-size:8.5px;line-height:20px;padding-left:6px;color:#444}
.nl-btn{left:401px;top:978px;width:41px;height:20px;background:var(--orange);color:#fff;font-size:9px;text-align:center;line-height:20px}
.date{color:var(--orange)}
.social-box{left:629px;top:980px;width:188px;height:177px;background:#fff;border:1px solid #bcc3d4}
.social-box .s{position:absolute;font-size:8px;color:#333}
.face{position:absolute;width:27px;height:27px;background:linear-gradient(#c9a48c,#8d6b5a)}
.bottom-rule{left:108px;top:1162px;width:709px;height:1px;background:#4a4340}
.copyright{left:110px;top:1172px;font-size:8.5px;color:#aaa}
.sq{position:absolute;top:1171px;width:11px;height:11px}
</style>
</head>
<body>

<div class="abs header-band"></div>
<div class="abs header-fade"></div>

<div class="abs brand">
  <div class="brand-mark"></div>
  <div class="brand-name">DWELL VANTORO<br>REAL ESTATE</div>
</div>

<form class="login" aria-label="Client login">
  <label style="left:461px;top:7px">User ID</label>
  <div class="field" style="left:461px;top:22px;width:150px"></div>
  <label style="left:618px;top:7px">Password</label>
  <div class="field" style="left:618px;top:22px;width:151px"></div>
  <div class="btn">Log in</div>
  <div class="check"></div>
  <label style="left:477px;top:47px">Remember me</label>
  <label style="left:618px;top:47px">Forgot your Password ? / Register</label>
</form>

<nav class="abs nav">
  <span>Home</span><span>Company</span><span>Associates</span><span>Search Properties</span><span>Marketing &amp;Design</span><span>Contact</span>
</nav>

<div class="abs slider"></div>
<div class="abs slide" role="img" aria-label="Featured property: large grey-blue suburban house with white porch and colourful garden"></div>
<div class="abs slider-shadow"></div>
<div class="abs arrow-btn" style="left:120px;top:264px"><svg width="10" height="14" viewBox="0 0 10 14"><path d="M8 1 2 7l6 6" fill="none" stroke="#222" stroke-width="2"/></svg></div>
<div class="abs arrow-btn" style="left:767px;top:264px"><svg width="10" height="14" viewBox="0 0 10 14"><path d="M2 1l6 6-6 6" fill="none" stroke="#222" stroke-width="2"/></svg></div>

<!-- property search -->
<div class="abs tab active" style="left:108px;width:112px">Property Search</div>
<div class="abs tab dark" style="left:223px;width:124px">Open House Search</div>
<div class="abs tab dark" style="left:350px;width:80px">Map Search</div>
<div class="abs search-panel">
  <div class="radio on" style="left:14px;top:15px"></div><div class="sp" style="left:30px;top:13px">For Sale</div>
  <div class="radio" style="left:14px;top:41px"></div><div class="sp" style="left:30px;top:40px">For Rent</div>
  <div class="sp" style="left:124px;top:16px">Property Type</div><div class="select" style="left:186px;top:16px;width:76px">Condominiums</div>
  <div class="sp" style="left:138px;top:41px">City Name</div><div class="select" style="left:186px;top:40px;width:76px">Miami Beach</div>
  <div class="sp" style="left:324px;top:16px">Price Min</div><div class="select" style="left:369px;top:16px;width:56px">$250.000</div>
  <div class="sp" style="left:324px;top:41px">Price Max</div><div class="select" style="left:369px;top:40px;width:56px">$5 M+</div>
  <div class="sp" style="left:495px;top:16px">Beds</div><div class="select" style="left:519px;top:16px;width:26px">1+</div>
  <div class="sp" style="left:492px;top:41px">Baths</div><div class="select" style="left:519px;top:40px;width:26px">1+</div>
  <div class="sp" style="left:620px;top:42px;font-size:8.5px;text-decoration:underline">Advanced Search</div>
</div>
<div class="abs search-btn">Property Search
  <svg width="14" height="14" viewBox="0 0 14 14"><circle cx="5.5" cy="5.5" r="4" fill="none" stroke="#1d4d05" stroke-width="2"/><path d="M8.5 8.5 13 13" stroke="#1d4d05" stroke-width="2.4"/></svg>
</div>

<!-- welcome -->
<div class="abs welcome-bar"><h2>WELCOME TO DWELL VANTORO</h2></div>
<p class="abs copy" style="top:628px">Lorem Ipsum is simply dummy text of the printing and typesetting industry. Lorem Ipsum has been the industry's standard dummy text ever since the 1500s, when an unknown printer took a of type and scrambled it to make a type specimen book.</p>
<p class="abs copy" style="top:681px">Lorem Ipsum comes from sections 1.10.32 and 1.10.33 of "de Finibus Bonorum et Malorum" (The Extremes of Good and Evil) by Aurelian, written in 45 BC. This book is a treatise on the theory of ethics, very popular during the Renaissance.</p>
<div class="abs more" style="left:412px;top:728px">Read More ➜</div>

<!-- news -->
<h2 class="abs news-title">LATEST NEWS</h2>
<div class="abs news-item" style="left:485px;top:620px;width:335px;height:44px">
  <svg width="45" height="44" viewBox="0 0 45 44"><rect x="1" y="5" width="43" height="38" rx="3" fill="#ebebeb" stroke="#bbb"/><rect x="1" y="5" width="43" height="11" rx="3" fill="#c8763a"/><rect x="11" y="1" width="3" height="8" fill="#666"/><rect x="31" y="1" width="3" height="8" fill="#666"/><text x="22.5" y="14" font-size="7" fill="#fff" text-anchor="middle" font-family="Open Sans,sans-serif">AUG</text><text x="22.5" y="35" font-size="16" fill="#222" text-anchor="middle" font-family="PT Serif,serif">21</text></svg>
  <h3>Lorem Ipsum is simply dummy text setting industry.</h3>
  <p>Lorem Ipsum is simply dummy text of the printing&nbsp; Ipsum has been the dummy text ever since the 1500s...</p>
</div>
<div class="abs news-item" style="left:485px;top:678px;width:335px;height:44px">
  <svg width="45" height="44" viewBox="0 0 45 44"><rect x="1" y="5" width="43" height="38" rx="3" fill="#ebebeb" stroke="#bbb"/><rect x="1" y="5" width="43" height="11" rx="3" fill="#c8763a"/><rect x="11" y="1" width="3" height="8" fill="#666"/><rect x="31" y="1" width="3" height="8" fill="#666"/><text x="22.5" y="14" font-size="7" fill="#fff" text-anchor="middle" font-family="Open Sans,sans-serif">AUG</text><text x="22.5" y="35" font-size="16" fill="#222" text-anchor="middle" font-family="PT Serif,serif">21</text></svg>
  <h3>Lorem Ipsum is simply dummy text setting industry.</h3>
  <p>Lorem Ipsum is simply dummy text of the printing&nbsp; Ipsum has been the dummy text ever since the 1500s...</p>
</div>
<div class="abs more" style="left:760px;top:728px">View All News ➜</div>

<div class="abs rule"></div>

<!-- gallery -->
<h2 class="abs gallery-title">PHOTO GALLERY</h2>
<div class="abs gal-arrow" style="left:112px;border-radius:0 22px 22px 0"><svg width="23" height="44" viewBox="0 0 23 44"><path d="M11 17l-5 5 5 5z" fill="#444"/></svg></div>
<div class="abs gal-arrow" style="left:790px;border-radius:22px 0 0 22px"><svg width="23" height="44" viewBox="0 0 23 44"><path d="M12 17l5 5-5 5z" fill="#444"/></svg></div>
<div class="abs thumb" style="left:156px"><div role="img" aria-label="White modern apartment building under blue sky" style="background:linear-gradient(#4b8fd6,#cfd9e0 55%,#6d8f4e)"></div></div>
<div class="abs thumb" style="left:316px"><div role="img" aria-label="Tall residential tower with balconies" style="background:linear-gradient(#3f7fcc,#b8c6d4 55%,#58743f)"></div></div>
<div class="abs thumb" style="left:476px"><div role="img" aria-label="Two-storey family house with front lawn" style="background:linear-gradient(#b9c6d2,#a39b90 55%,#5d8a3c)"></div></div>
<div class="abs thumb" style="left:636px"><div role="img" aria-label="Victorian style house surrounded by trees" style="background:linear-gradient(#c7d3da,#a9ad9f 50%,#46772e)"></div></div>
<div class="abs gal-shadow"></div>

<!-- footer -->
<footer class="abs footer"></footer>
<div class="abs newsletter">Sign Up Our Newsletter!</div>
<div class="abs nl-field">Enter Your E-mail...</div>
<div class="abs nl-btn">Sign Up</div>

<div class="f-head" style="left:109px;top:1031px">Quick Links</div>
<div class="f" style="left:109px;top:1049px">Home<br>Company<br>Associates<br>Search Properties<br>Marketing &amp;Design<br>Contact</div>

<div class="f-head" style="left:250px;top:1031px">Contact Us</div>
<div class="f" style="left:255px;top:1049px">012 Lorem Ipsum,<br>dummy text.<br>(000) 123-4567 Phone<br>(000) 123-4567 Fax<br><span style="color:var(--orange)">Email-info@vantorohomes.net</span></div>

<div class="f-head" style="left:446px;top:1031px">Recent Blog Post</div>
<div class="f" style="left:446px;top:1050px"><span class="date">12 March, 2012</span><br>Lorem Ipsum is simply dummy text...</div>
<div class="f" style="left:446px;top:1090px"><span class="date">12 March, 2012</span><br>Lorem Ipsum is simply dummy text...</div>
<div class="f" style="left:446px;top:1129px"><span class="date">12 March, 2012</span><br>Lorem Ipsum is simply dummy text...</div>

<aside class="abs social-box" aria-label="Chatterloop social plugin">
  <div style="position:absolute;left:7px;top:7px;width:28px;height:28px;background:#2a2522"></div>
  <div class="s" style="left:51px;top:9px"><b style="color:#3b5998">Dwell Vantoro</b> on Chatterloop</div>
  <div class="s" style="left:45px;top:24px;border:1px solid #aaa;background:#eee;padding:1px 6px">Like</div>
  <div class="s" style="left:136px;top:21px;border:1px solid #4a7d24;background:linear-gradient(#8fd04f,#4b9a1b);color:#fff;font-weight:600;font-size:9px;padding:3px 5px">Sign Up</div>
  <div style="position:absolute;left:5px;top:46px;width:176px;height:1px;background:#ddd"></div>
  <div class="s" style="left:7px;top:50px">560 people like &nbsp;<b>Dwell Vantoro</b></div>
  <div class="face" style="left:8px;top:66px"></div><div class="face" style="left:47px;top:66px"></div><div class="face" style="left:87px;top:66px"></div><div class="face" style="left:126px;top:66px"></div>
  <div class="s" style="left:7px;top:95px">Tessa</div><div class="s" style="left:46px;top:95px">Orin</div><div class="s" style="left:86px;top:95px">Lorena</div><div class="s" style="left:126px;top:95px">Celia</div>
  <div class="face" style="left:8px;top:115px"></div><div class="face" style="left:47px;top:115px"></div><div class="face" style="left:87px;top:115px"></div><div class="face" style="left:126px;top:115px"></div>
  <div class="s" style="left:7px;top:145px">Nina</div><div class="s" style="left:46px;top:145px">Dario</div><div class="s" style="left:86px;top:145px">Ivana</div><div class="s" style="left:126px;top:145px">Milo</div>
  <div style="position:absolute;left:5px;top:159px;width:176px;height:1px;background:#ddd"></div>
  <div style="position:absolute;left:7px;top:164px;width:8px;height:8px;background:#3b5998"></div>
  <div class="s" style="left:19px;top:162px;font-size:7px;color:#555">Chatterloop social plugin</div>
</aside>

<div class="abs bottom-rule"></div>
<div class="abs copyright">© 2012 Dwell Vantoro. | All Rights Reserved.</div>
<div class="sq" style="left:766px;background:#3b5998"></div>
<div class="sq" style="left:786px;background:#3aa5dc"></div>
<div class="sq" style="left:806px;background:#1b83b7"></div>

</body>
</html>
```